Corvena Hotel, city center modern minimal hotel operating all year round, on Rhodes island Greece

city, modern ,all year operating hotel

Target Market(s)

tourists, business agents

Industry/Entity Type

tourism

Coding

Coded - Design and coding required

Number of Pages Required

2 page

Requirements
Must have
• room type photos and descriptions, amenities individual listing (graphic), comments sections, map driving location details
Nice to have
• gallery section, modern and minimal design, amenities section, individual room type descriptions, photos and facilities

```html
<!DOCTYPE html>
<html lang="en">
<head>
<meta charset="utf-8">
<title>Corvena Hotel — Rhodes</title>
<link rel="stylesheet" href="https://fonts.googleapis.com/css2?family=EB+Garamond:wght@400;500;600&display=swap">
<style>
:root{
  --green:#1f4a35;
  --green-dark:#173a29;
  --gold:#c9a44a;
  --gold-light:#e0c47c;
  --cream:#fbf8ee;
  --cream-deep:#f6f0dc;
  --ink:#2b2b2b;
  --muted:#6b6b6b;
  --charcoal:#262626;
  --white:#ffffff;
}
*{box-sizing:border-box;margin:0;padding:0}
html,body{width:1200px;height:4156px;overflow:hidden}
body{position:relative;background:var(--cream);font-family:"EB Garamond",Georgia,serif;color:var(--ink);font-size:15px;line-height:1.45}
.abs{position:absolute}
.photo{position:absolute}
.btn{position:absolute;display:flex;align-items:center;justify-content:center;font-size:13px;letter-spacing:.3px}
.btn-green{background:var(--green);color:var(--white)}
.btn-gold{background:var(--gold);color:var(--white)}
.btn-outline{border:1px solid var(--gold);color:var(--ink);background:var(--white)}
.btn-outline-light{border:1px solid var(--gold);color:var(--gold)}
.section-title{position:absolute;left:0;width:1200px;text-align:center;font-size:26px;font-weight:500}

/* header */
.site-header{left:0;top:0;width:1200px;height:48px;background:var(--white);z-index:3}
.brand{left:24px;top:8px;display:flex;align-items:center;gap:8px;font-size:24px;font-weight:600;color:var(--green)}
.brand-mark{width:28px;height:28px;background:var(--gold)}
.main-nav{left:330px;top:14px;display:flex;gap:34px;font-size:14px}
.social{right:120px;top:14px;display:flex;gap:8px}
.social span{width:20px;height:20px;border-radius:50%;background:var(--green)}
.lang{right:28px;top:14px;font-size:14px;display:flex;gap:6px;align-items:center}
.lang i{display:inline-block;width:18px;height:12px;background:#9aa7c8}

/* hero */
.hero-photo{left:0;top:0;width:1200px;height:604px;background:linear-gradient(180deg,#5a86c0 0%,#9ab9dc 35%,#dfe6ee 60%,#cfd3d6 100%)}
.hero-card{left:236px;top:220px;width:330px;height:260px;background:rgba(255,255,255,.93);padding:34px 32px}
.hero-card h1{font-size:30px;font-weight:500;text-align:center;margin-bottom:14px}
.hero-card p{font-size:12.5px;color:var(--muted);line-height:1.5}
.booking-bar{left:200px;top:556px;width:800px;height:92px;background:var(--green);color:var(--white)}
.field-label{position:absolute;top:16px;font-size:13px}
.field{position:absolute;top:40px;height:28px;background:var(--white);color:var(--ink);font-size:12px;display:flex;align-items:center;padding:0 8px;justify-content:space-between}

/* welcome */
.welcome-text{left:400px;top:768px;width:400px;text-align:center;font-size:13px;color:var(--muted)}
.gallery-strip{left:228px;top:880px;width:744px;height:200px;display:flex;gap:6px}
.gallery-tile{position:relative;flex:1}
.gallery-tile span{position:absolute;left:0;right:0;bottom:14px;text-align:center;color:var(--white);font-size:13px}

/* rooms */
.room-title{font-size:36px;font-weight:500;color:var(--gold)}
.price{font-size:13px;color:var(--muted)}
.room-text{font-size:13px;color:var(--muted);line-height:1.55}
.thumb-row{display:flex;gap:6px}
.thumb-row div{flex:1}
.view-gallery{background:var(--green);color:var(--white);font-size:12px;display:flex;align-items:center;justify-content:center;flex-direction:column;gap:8px}
.dots{display:flex;gap:8px}
.dots i{width:8px;height:8px;border-radius:50%;background:rgba(255,255,255,.6)}
.dots i.on{background:var(--white)}

/* amenities */
.amenities-band{left:0;top:2180px;width:1200px;height:348px;background:var(--cream-deep)}
.amenities-list{left:258px;top:2256px;list-style:none}
.amenities-list li{display:flex;align-items:center;gap:22px;font-size:14px;height:40px}
.amenities-list svg{width:22px;height:22px}

/* contact form */
.contact-card{left:640px;top:2608px;width:360px;height:384px;background:var(--green);color:var(--white);padding:22px 26px}
.contact-card h2{font-size:26px;font-weight:500;text-align:center}
.contact-card .sub{font-size:12px;text-align:center;margin-bottom:16px}
.input{background:var(--white);color:var(--muted);font-size:11px;padding:4px 8px;height:24px;margin-bottom:14px}

/* contact details */
.contact-row{left:228px;top:3062px;width:744px;display:flex;justify-content:space-between;font-size:13px}
.contact-row div{display:flex;align-items:center;gap:10px}
.map{left:228px;top:3112px;width:744px;height:336px;background:linear-gradient(135deg,#2c2f33,#3b3f44)}
.map-bar{left:228px;top:3408px;width:744px;height:40px;background:var(--green);color:var(--white);font-size:13px}

/* reviews */
.reviews{left:0;top:3540px;width:1200px;height:320px;background:linear-gradient(180deg,#2f5a43 0%,#1f4a35 60%,#173a29 100%)}
.reviews h2{position:absolute;top:30px;width:1200px;text-align:center;color:var(--white);font-size:26px;font-weight:500}
.reviews blockquote{position:absolute;left:400px;top:92px;width:400px;text-align:center;color:var(--white);font-size:14px;line-height:1.5}

/* footer */
.site-footer{left:0;top:3860px;width:1200px;height:296px;background:var(--charcoal);color:var(--white)}
.footer-col{position:absolute;top:62px;font-size:13px;line-height:1.75}
.footer-col h3{font-size:20px;font-weight:500;margin-bottom:6px}
.footer-copy{position:absolute;top:268px;width:1200px;text-align:center;font-size:11px;color:#8a8a8a}
</style>
</head>
<body>

<header class="abs site-header">
  <div class="abs brand"><span class="brand-mark"></span>Corvena Hotel</div>
  <nav class="abs main-nav"><span>Home</span><span>Accommodations</span><span>Reviews</span><span>Gallery</span><span>About us</span><span>Contact</span></nav>
  <div class="abs social"><span></span><span></span><span></span><span></span></div>
  <div class="abs lang">English <i></i></div>
</header>

<div class="photo hero-photo" role="img" aria-label="Whitewashed island houses with blue domes overlooking the sea"></div>
<div class="abs hero-card">
  <h1>Experience Greece</h1>
  <p>Stay in the heart of Rhodes town with calm modern rooms, warm service and easy access to beaches, old streets and the harbour all year round.</p>
  <div class="btn btn-green" style="left:32px;top:178px;width:96px;height:34px">Book Today</div>
  <div class="btn btn-outline" style="left:196px;top:178px;width:96px;height:34px">More Details</div>
</div>

<section class="abs booking-bar">
  <span class="field-label" style="left:68px">Arrival</span>
  <div class="field" style="left:68px;width:140px">dd/mm/yyyy
    <svg width="14" height="14" viewBox="0 0 14 14"><rect x="1" y="2" width="12" height="11" fill="none" stroke="#1f4a35"/><line x1="1" y1="5" x2="13" y2="5" stroke="#1f4a35"/></svg></div>
  <span class="field-label" style="left:258px">Departure</span>
  <div class="field" style="left:258px;width:140px">dd/mm/yyyy
    <svg width="14" height="14" viewBox="0 0 14 14"><rect x="1" y="2" width="12" height="11" fill="none" stroke="#1f4a35"/><line x1="1" y1="5" x2="13" y2="5" stroke="#1f4a35"/></svg></div>
  <span class="field-label" style="left:428px">Persons</span>
  <div class="field" style="left:428px;width:100px">2 <span>▾</span></div>
  <div class="btn btn-gold" style="left:592px;top:40px;width:138px;height:28px">Check Availability</div>
</section>

<h2 class="section-title" style="top:720px">Welcome to Corvena Hotel</h2>
<p class="abs welcome-text">A modern city hotel in central Rhodes, open every season. Quiet rooms, thoughtful amenities and friendly staff make it an easy base for travellers and business guests exploring the island.</p>

<div class="abs gallery-strip">
  <div class="gallery-tile" style="background:linear-gradient(160deg,#c89a52,#6b4a26)" role="img" aria-label="Afternoon drinks served on a terrace"><span>Afternoon Snacks</span></div>
  <div class="gallery-tile" style="background:linear-gradient(160deg,#7d8a88,#2f3b3a)" role="img" aria-label="Glass roofed hotel lounge"><span>Spacious Lounge</span></div>
  <div class="gallery-tile" style="background:linear-gradient(160deg,#6f6a5c,#2d2a24)" role="img" aria-label="Indoor pool in the evening"><span>Private Pools</span></div>
  <div class="gallery-tile" style="background:linear-gradient(160deg,#8fb7c6,#3b6e7a)" role="img" aria-label="Outdoor pool with loungers"><span>Pool Access</span></div>
</div>

<!-- Deluxe Suite -->
<div class="photo" style="left:100px;top:1188px;width:520px;height:372px;background:linear-gradient(160deg,#c9c3b8,#7b6f60)" role="img" aria-label="Deluxe suite bedroom with armchair and large bed"></div>
<div class="abs dots" style="left:330px;top:1528px"><i class="on"></i><i></i><i></i><i></i></div>
<div class="abs" style="left:648px;top:1190px">
  <div class="room-title">Deluxe Suite</div>
  <div class="price">€ 2p.p/n</div>
</div>
<p class="abs room-text" style="left:648px;top:1276px;width:300px">Relax in a spacious suite with a private seating area, city views and a large bed. Fresh linen, coffee corner, toiletries and daily cleaning are included.</p>
<div class="btn btn-outline" style="left:648px;top:1368px;width:118px;height:30px">Check Availability</div>
<div class="abs thumb-row" style="left:620px;top:1440px;width:468px;height:120px">
  <div style="background:linear-gradient(160deg,#a88c6a,#5d4631)" role="img" aria-label="Suite sitting area"></div>
  <div style="background:linear-gradient(160deg,#b7a48a,#6c5b44)" role="img" aria-label="Suite bathroom"></div>
  <div class="view-gallery">View Gallery
    <svg width="22" height="24" viewBox="0 0 22 24"><path d="M3 2 L3 20 L8 15 L12 23 L15 21 L11 14 L18 14 Z" fill="#fff"/></svg></div>
</div>

<!-- Junior Suite -->
<div class="abs" style="left:240px;top:1640px">
  <div class="room-title">Junior Suite</div>
  <div class="price">€ 2p.p/n</div>
</div>
<p class="abs room-text" style="left:240px;top:1740px;width:320px">Relax in a cosy suite with warm light and a comfortable queen bed.</p>
<div class="btn btn-outline" style="left:240px;top:1808px;width:118px;height:30px">Check Availability</div>
<div class="photo" style="left:600px;top:1640px;width:488px;height:380px;background:linear-gradient(160deg,#d2c4b0,#8a6a48)" role="img" aria-label="Junior suite bedroom with wooden furniture"></div>
<div class="abs thumb-row" style="left:228px;top:1888px;width:372px;height:132px">
  <div style="background:linear-gradient(160deg,#b9ac98,#6e604c)" role="img" aria-label="Junior suite bed"></div>
  <div style="background:linear-gradient(160deg,#a5906f,#5a4630)" role="img" aria-label="Junior suite desk"></div>
  <div class="view-gallery">View Gallery
    <svg width="22" height="24" viewBox="0 0 22 24"><path d="M3 2 L3 20 L8 15 L12 23 L15 21 L11 14 L18 14 Z" fill="#fff"/></svg></div>
</div>
<div class="btn btn-gold" style="left:428px;top:2036px;width:352px;height:34px">View Room Details</div>

<!-- Amenities -->
<div class="abs amenities-band"></div>
<h2 class="abs" style="left:264px;top:2196px;font-size:26px;font-weight:500">Our Amenities</h2>
<ul class="abs amenities-list">
  <li><svg viewBox="0 0 22 22"><path d="M4 3 H18 L11 11 Z M11 11 V19 M7 19 H15" fill="none" stroke="#2b2b2b" stroke-width="1.6"/></svg>Evening Bar</li>
  <li><svg viewBox="0 0 22 22"><circle cx="11" cy="12" r="7" fill="none" stroke="#2b2b2b" stroke-width="1.6"/><path d="M2 3 V10 M20 3 V19" stroke="#2b2b2b" stroke-width="1.6"/></svg>Complimentary meals</li>
  <li><svg viewBox="0 0 22 22"><path d="M3 14 L5 8 H17 L19 14 V17 H3 Z" fill="none" stroke="#2b2b2b" stroke-width="1.6"/><circle cx="7" cy="17" r="2" fill="#2b2b2b"/><circle cx="15" cy="17" r="2" fill="#2b2b2b"/></svg>Private Cars</li>
  <li><svg viewBox="0 0 22 22"><path d="M2 9 Q11 1 20 9 M5 12 Q11 7 17 12 M8 15 Q11 12.5 14 15" fill="none" stroke="#2b2b2b" stroke-width="1.6"/><circle cx="11" cy="18" r="1.5" fill="#2b2b2b"/></svg>Free Wifi</li>
  <li><svg viewBox="0 0 22 22"><path d="M2 14 Q5 11 8 14 T14 14 T20 14 M2 18 Q5 15 8 18 T14 18 T20 18" fill="none" stroke="#2b2b2b" stroke-width="1.6"/><path d="M8 12 V3 H12" fill="none" stroke="#2b2b2b" stroke-width="1.6"/></svg>Pool access</li>
</ul>
<div class="photo" style="left:592px;top:2180px;width:512px;height:348px;background:linear-gradient(160deg,#4c8c6a,#5fb0c8 55%,#2a7fa0)" role="img" aria-label="Guests relaxing at the edge of the pool"></div>

<!-- Get in touch -->
<div class="photo" style="left:188px;top:2624px;width:452px;height:316px;background:linear-gradient(160deg,#e6d7c0,#a98f6c)" role="img" aria-label="Guest enjoying breakfast on a sunny terrace"></div>
<section class="abs contact-card">
  <h2>Get In Touch</h2>
  <p class="sub">Have a question? We love to hear from you.</p>
  <div class="input">Name*</div>
  <div class="input">Email*</div>
  <div class="input" style="height:104px">Message</div>
  <div class="btn btn-gold" style="left:246px;top:320px;width:86px;height:30px">Send</div>
</section>

<!-- Contact -->
<h2 class="section-title" style="top:3006px">Contact</h2>
<div class="abs contact-row">
  <div><svg width="16" height="18" viewBox="0 0 16 18"><path d="M8 17 C3 11 2 8 2 6.5 A6 6 0 0 1 14 6.5 C14 8 13 11 8 17 Z" fill="#2b2b2b"/><circle cx="8" cy="6.5" r="2" fill="#fbf8ee"/></svg>14 Kallirois Street, Rhodes, Greece</div>
  <div><svg width="18" height="18" viewBox="0 0 18 18"><circle cx="9" cy="9" r="9" fill="#2b2b2b"/><path d="M6 5 L8 7 L7 8.5 Q8 10.5 9.5 11 L11 10 L13 12 L12 13.5 Q8 13 5 8 Z" fill="#fff"/></svg>+30 2241 000 418</div>
  <div><svg width="18" height="18" viewBox="0 0 18 18"><circle cx="9" cy="9" r="9" fill="#2b2b2b"/><rect x="4.5" y="6" width="9" height="6.5" fill="none" stroke="#fff"/><path d="M4.5 6 L9 10 L13.5 6" fill="none" stroke="#fff"/></svg>info@corvenahotel.com</div>
</div>
<div class="photo map" role="img" aria-label="Street map of Rhodes town with the hotel location marked"></div>
<div class="abs" style="left:244px;top:3124px;font-size:12px;color:var(--gold)">Rhodes Town</div>
<div class="abs map-bar">
  <span class="abs" style="left:94px;top:10px">Type in your address</span>
  <div class="abs" style="left:228px;top:8px;width:284px;height:24px;background:var(--white)"></div>
  <div class="btn btn-gold" style="left:540px;top:8px;width:150px;height:24px">Get Directions</div>
</div>
<div class="btn btn-gold" style="left:544px;top:3466px;width:112px;height:30px">Route Details</div>

<!-- Reviews -->
<section class="abs reviews">
  <h2>Customer Reviews</h2>
  <blockquote>“A calm, spotless hotel right in the centre of town. The rooms were modern and quiet, breakfast was generous and the staff helped us plan every day trip. We would gladly return again next season.”<br><br><span style="font-size:13px">— Lena M.</span></blockquote>
  <div class="abs dots" style="left:576px;top:270px"><i class="on"></i><i></i><i></i><i></i></div>
</section>

<!-- Footer -->
<footer class="abs site-footer">
  <div class="footer-col" style="left:228px;top:40px;width:170px">
    <div style="width:34px;height:34px;background:var(--gold);margin:0 0 10px 36px"></div>
    <p style="font-size:12px;line-height:1.5;margin-bottom:14px">A modern city hotel in Rhodes, open all year for leisure and business.</p>
    <p style="font-size:12px;line-height:1.6">+30 2241 000 418<br>info@corvenahotel.com<br>14 Kallirois Street, Rhodes, Greece</p>
  </div>
  <div class="footer-col" style="left:432px"><h3>About</h3>About Us<br>Careers<br>Press</div>
  <div class="footer-col" style="left:540px"><h3>Connect</h3>Photo Journal<br>Community<br>Updates<br>Careers</div>
  <div class="footer-col" style="left:672px"><h3>Company</h3>We Hire<br>Privacy<br>Terms</div>
  <div class="footer-col" style="left:808px;width:170px"><h3>Newsletter</h3><span style="font-size:12px;line-height:1.4;display:block">Subscribe to our newsletter to stay updated.</span>
    <div style="display:flex;margin-top:10px"><div style="width:120px;height:22px;background:var(--white);color:var(--muted);font-size:11px;padding:3px 6px">Email</div><div style="width:40px;height:22px;background:var(--gold)"></div></div>
  </div>
  <p class="footer-copy">© Corvena Hotel. All rights reserved.</p>
</footer>

</body>
</html>
```